Ozark Hollowpine Barbeque Sauce*

Design a branded label for a bottle of sauce..... for OZARK HOLLOWPINE BBQ
FOOD LABEL. Target audience is woman buying bbq sauce for men. There is a lot of competition in the market so Texas should really be a highlight. LOGO SHOULD BE BIG. PLEASE RECREATE IF YOU CAN.

I am looking for a unique die cut....

Target Market(s)

GENERAL GROCERY STORE

Industry/Entity Type

Retail

Colors
f58946
ec1f27
f78f20
fee18a
f48541

Requirements
Must have
• OZARK HOLLOWPINE BBQ SAUCE
Nice to have
• ILLUSTRATIONS
Should not have
• NO PICTURES BUT

```html
<!DOCTYPE html>
<html lang="en">
<head>
<meta charset="utf-8">
<title>Ozark Hollowpine BBQ Sauce – Label</title>
<link rel="stylesheet" href="https://fonts.googleapis.com/css2?family=Lato:wght@400;700;900&family=Oswald:wght@500&family=Archivo+Narrow:wght@400;700&display=swap">
<style>
  :root {
    --page: #e4e5e6;
    --label-black: #0d0d0d;
    --ink: #231f20;
    --paper: #ffffff;
    --fire-red: #ec1f27;
    --fire-orange: #f78f20;
    --fire-amber: #f58946;
    --fire-yellow: #fee18a;
    --muted: #d9d9d9;
  }
  * { box-sizing: border-box; margin: 0; padding: 0; }
  html, body { width: 1200px; height: 1026px; overflow: hidden; background: var(--page); }
  .label-wrap {
    position: absolute; left: 40px; top: 293px; width: 1120px; height: 440px;
    background: var(--label-black); display: flex; color: var(--paper);
    font-family: "Lato", sans-serif;
  }
  .panel { position: relative; height: 100%; }
  .panel--info { width: 350px; padding: 70px 28px 0 34px; }
  .panel--front { width: 420px; }
  .panel--facts { width: 350px; }

  .info-title { font-size: 15px; font-weight: 400; letter-spacing: .02em; margin-bottom: 10px; }
  .info-copy { font-size: 10px; line-height: 1.25; text-align: justify; }
  .info-box { border: 1.5px solid var(--paper); padding: 7px 8px; margin: 14px 0; }
  .info-dates { display: flex; gap: 18px; margin-top: 28px; font-size: 10px; }
  .info-dates .blank { width: 110px; height: 62px; background: var(--paper); }
  .info-dates ul { list-style: none; line-height: 2.9; }

  .front-badge { position: absolute; left: 10px; top: 30px; width: 400px; height: 380px; }
  .front-text { position: absolute; left: 10px; top: 30px; width: 400px; height: 380px; text-align: center; color: var(--ink); }
  .brand-name {
    position: absolute; left: 0; right: 0; top: 96px;
    display: flex; justify-content: center; align-items: center; gap: 10px;
    font-family: "Lato", sans-serif; font-weight: 900; font-size: 26px; letter-spacing: .04em; line-height: 1.1;
  }
  .brand-name .dot { width: 16px; height: 16px; border-radius: 50%; background: var(--fire-red); flex: none; }
  .brand-name span.words { display: block; }
  .product-name {
    position: absolute; left: 0; right: 0; top: 212px;
    font-family: "Oswald", sans-serif; font-weight: 500; font-size: 72px; line-height: 1; letter-spacing: -.01em;
  }
  .net-weight { position: absolute; left: 0; right: 0; top: 306px; font-size: 15px; font-weight: 700; line-height: 1.2; color: #333; }

  .cert-list { position: absolute; left: 36px; top: 66px; list-style: none; width: 70px; text-align: center; }
  .cert-list li { margin-bottom: 20px; font-size: 9px; }
  .cert-mark { display: block; width: 30px; height: 30px; margin: 0 auto 5px; border: 2px solid var(--paper); border-radius: 50%; }

  .nutrition {
    position: absolute; left: 126px; top: 66px; width: 200px; height: 276px;
    background: var(--paper); color: #000; font-family: "Archivo Narrow", sans-serif;
    padding: 5px 6px; font-size: 8px; line-height: 1.35;
  }
  .nutrition h2 { font-size: 20px; font-weight: 700; letter-spacing: .04em; line-height: 1; border-bottom: 1px solid #000; }
  .nutrition .rule-thick { border-top: 5px solid #000; margin: 2px 0; }
  .nutrition .rule-mid { border-top: 3px solid #000; margin: 2px 0; }
  .nutrition .row { display: flex; justify-content: space-between; border-bottom: .5px solid #999; }
  .nutrition .row.sub { padding-left: 12px; }
  .nutrition b { font-weight: 700; }
  .nutrition .right { text-align: right; font-size: 6px; }
  .nutrition .foot { font-size: 6px; line-height: 1.3; margin-top: 3px; }
  .nutrition table { width: 100%; font-size: 6px; border-collapse: collapse; margin-top: 2px; border-top: .5px solid #000; }
  .nutrition td { padding: 0; }
</style>
</head>
<body>
<main class="label-wrap">

  <section class="panel panel--info">
    <h3 class="info-title">LOREM IPSUM</h3>
    <p class="info-copy">Lorem ipsum dolor sit amet, consectetuer adipiscing elit, sed diam nonummy nibh euismod tincidunt ut laoreet dolore magna aliquam erat volutpat. Ut wisi enim ad minim veniam, quis nostrud exerci tation ullamcorper suscipit lobortis nisl ut aliquip ex ea commodo consequat. Duis autem vel eum iriure dolor.</p>
    <p class="info-copy info-box">Lorem ipsum dolor sit amet, consectetuer adipiscing elit, sed diam nonummy nibh euismod tincidunt ut laoreet dolore magna aliquam erat volutpat. Ut wisi enim ad minim veniam.</p>
    <p class="info-copy">Lorem ipsum dolor sit amet, consectetuer adipiscing elit, sed diam nonummy nibh euismod tincidunt ut laoreet dolore magna aliquam erat volutpat. Ut wisi enim ad minim veniam</p>
    <div class="info-dates">
      <div class="blank"></div>
      <ul><li>Issue Date:</li><li>Exp Date:</li></ul>
    </div>
  </section>

  <section class="panel panel--front">
    <svg class="front-badge" viewBox="0 0 400 380" aria-hidden="true">
      <defs>
        <linearGradient id="fireBand" x1="0" y1="0" x2="0" y2="1">
          <stop offset="0" stop-color="var(--fire-red)"/>
          <stop offset=".55" stop-color="var(--fire-orange)"/>
          <stop offset="1" stop-color="var(--fire-yellow)"/>
        </linearGradient>
        <clipPath id="innerHex">
          <polygon points="200,22 377,106 377,274 200,358 23,274 23,106"/>
        </clipPath>
      </defs>
      <polygon points="200,4 394,96 394,284 200,376 6,284 6,96" fill="var(--paper)"/>
      <polygon points="200,14 385,101 385,279 200,366 15,279 15,101" fill="var(--label-black)"/>
      <polygon points="200,22 377,106 377,274 200,358 23,274 23,106" fill="var(--paper)"/>
      <rect x="0" y="206" width="400" height="90" fill="url(#fireBand)" clip-path="url(#innerHex)"/>
    </svg>
    <div class="front-text">
      <p class="brand-name"><i class="dot"></i><span class="words">OZARK HOLLOWPINE<br>BBQ</span></p>
      <h1 class="product-name">BBQ SAUCE</h1>
      <p class="net-weight">Net wt 11 Oz<br>(312g)</p>
    </div>
  </section>

  <section class="panel panel--facts">
    <ul class="cert-list">
      <li><i class="cert-mark"></i>Gluten Free</li>
      <li><i class="cert-mark"></i>Non GMO</li>
      <li><i class="cert-mark"></i>Halal Certified</li>
      <li><i class="cert-mark"></i>Kosher Certified</li>
    </ul>
    <div class="nutrition">
      <h2>Nutrition Facts</h2>
      <div>Serving Size 1 (44g)</div>
      <div class="rule-thick"></div>
      <div style="font-size:6px"><b>Amount Per Serving</b></div>
      <div class="row"><b>Calories 96</b></div>
      <div class="rule-mid"></div>
      <div class="right">% Daily Value*</div>
      <div class="row"><span><b>Total Fat</b> 1g</span><b>2%</b></div>
      <div class="row sub"><span>Saturated Fat 0g</span><b>0%</b></div>
      <div class="row sub"><span>Trans Fat 0g</span></div>
      <div class="row"><span><b>Cholesterol</b> 0mg</span><b>0%</b></div>
      <div class="row"><span><b>Sodium</b> 1mg</span><b>0%</b></div>
      <div class="row"><span><b>Total Carbohydrate</b> 22g</span><b>7%</b></div>
      <div class="row sub"><span>Dietary Fiber 0g</span><b>0%</b></div>
      <div class="row sub"><span>Sugars 6g</span></div>
      <div class="row"><span><b>Protein</b> 1g</span><b>2%</b></div>
      <div class="rule-thick"></div>
      <p class="foot">*Percent Daily Values are based on a 2,000 calorie diet. Your daily values may be higher or lower depending on your needs.</p>
      <table>
        <tr><td></td><td>Calories</td><td>2,000</td><td>2,500</td></tr>
        <tr><td>Total Fat</td><td>Less than</td><td>65g</td><td>80g</td></tr>
        <tr><td>Sat Fat</td><td>Less than</td><td>20g</td><td>25g</td></tr>
        <tr><td>Cholesterol</td><td>Less than</td><td>300mg</td><td>300mg</td></tr>
        <tr><td>Sodium</td><td>Less than</td><td>2400mg</td><td>2400mg</td></tr>
        <tr><td>Total Carbohydrate</td><td></td><td>300g</td><td>375g</td></tr>
        <tr><td>Dietary Fiber</td><td></td><td>25g</td><td>30g</td></tr>
      </table>
    </div>
  </section>

</main>
</body>
</html>
```